Business Cards for Communications Technology Company

We are an innovative software company based in Tropical North Queensland, Australia. We have several brands with a focus on communications software for businesses. We are looking for a business card that is very innovate and creative whilst still remaining professional on a corporate level.

Our internal culture is very progressive and expresses a blend between the clarity of our natural surroundings and the highly technological industry we work in. Our current branding blends a modern minimalist typeface with the desire to push the boundaries in the way we communicate.

This is a corporate level business card for the communications software industry and may possibly also encompass our brands PelNetwork, PelCopy, PelPost and our B2B marketing service—with our companies name being Tarvix Holdings. Showing other brands on the business card is optional not compulsory.

Technical notes:

-We will attach all logo's and some examples of our corporate branding
- Would be willing to print with various papers, embossed, metallic ink, curved edges etc. in a standard business card size

Sample content:

Dorian Malcott
Senior Account Manager
Phone: 1300 482 916 / +617 4385 2604
Email: d.malcott@tarvix.com.au
Web: www.tarvix.com.au

Sincerely,
Tarvix Holdings.

```html
<!DOCTYPE html>
<html lang="en">
<head>
<meta charset="utf-8">
<title>Tarvix Holdings – Business Card</title>
<link href="https://fonts.googleapis.com/css2?family=Source+Sans+3:wght@400;600&display=swap" rel="stylesheet">
<style>
  :root {
    --backdrop: #2e2e2e;
    --card-white: #f4f4f2;
    --card-black: #161616;
    --brand-green: #5a9a2a;
    --text-grey: #4a4a4a;
    --divider: #dcdcda;
    --silver: #b9bcbf;
    --mark-grey: #8a8d90;
  }
  * { box-sizing: border-box; margin: 0; padding: 0; }
  html, body {
    width: 1200px; height: 900px; overflow: hidden;
    background: var(--backdrop);
    font-family: "Source Sans 3", "Myriad Pro", Arial, sans-serif;
  }
  .card-set {
    position: relative; width: 1200px; height: 900px;
  }
  .card {
    position: absolute; top: 290px;
    width: 520px; height: 316px;
    border-radius: 26px;
    box-shadow: 0 18px 40px rgba(0,0,0,.45);
  }
  /* Front */
  .card-front {
    left: 50px;
    background: var(--card-white);
    display: flex; align-items: center;
  }
  .front-brand {
    width: 232px; height: 100%;
    display: flex; flex-direction: column; align-items: center; justify-content: center;
    gap: 14px;
  }
  .brand-dot {
    width: 96px; height: 96px; border-radius: 50%;
    background: var(--mark-grey);
  }
  .brand-name {
    font-weight: 600; font-size: 17px; color: var(--mark-grey);
    letter-spacing: .5px;
  }
  .front-divider {
    width: 1px; height: 170px; background: var(--divider);
  }
  .front-details {
    padding-left: 26px;
    color: var(--text-grey);
  }
  .person-name {
    color: var(--brand-green); font-weight: 600; font-size: 21px; line-height: 1.1;
  }
  .person-title {
    font-size: 15px; margin-bottom: 14px;
  }
  .contact-list { list-style: none; font-size: 14.5px; line-height: 1.55; }
  .contact-list li { display: flex; align-items: center; gap: 8px; }
  .contact-list svg { width: 11px; height: 11px; fill: var(--brand-green); flex: none; }
  .sep { color: var(--brand-green); margin: 0 4px; }
  /* Back */
  .card-back {
    left: 630px;
    background: var(--card-black);
    display: flex; align-items: center; justify-content: center; gap: 14px;
  }
  .back-dot {
    width: 40px; height: 40px; border-radius: 50%; background: var(--silver);
  }
  .back-name {
    font-weight: 600; font-size: 32px; color: var(--silver); letter-spacing: 1px;
  }
</style>
</head>
<body>
<main class="card-set">
  <section class="card card-front" aria-label="Business card front">
    <div class="front-brand">
      <span class="brand-dot"></span>
      <span class="brand-name">Tarvix Holdings</span>
    </div>
    <div class="front-divider"></div>
    <div class="front-details">
      <h1 class="person-name">Dorian Malcott</h1>
      <p class="person-title">Senior Account Manager</p>
      <ul class="contact-list">
        <li><svg viewBox="0 0 12 12" aria-hidden="true"><path d="M2.4 0.6 4.2 2.8 3.3 4.2C3.9 5.7 5.2 7.2 7.8 8.7L9.2 7.8 11.4 9.6 10.3 11.4C5.5 11 1 6.5 0.6 1.7Z"/></svg>1300 482 916<span class="sep">/</span>+617 4385 2604</li>
        <li><svg viewBox="0 0 12 12" aria-hidden="true"><path d="M0 2h12v1.2L6 7 0 3.2Z"/><path d="M0 4.6 6 8.4 12 4.6V10H0Z"/></svg>d.malcott@tarvix.com.au</li>
        <li><svg viewBox="0 0 12 12" aria-hidden="true"><circle cx="6" cy="6" r="6"/></svg>www.tarvix.com.au</li>
      </ul>
    </div>
  </section>
  <section class="card card-back" aria-label="Business card back">
    <span class="back-dot"></span>
    <span class="back-name">Tarvix Holdings</span>
  </section>
</main>
</body>
</html>
```